Real Estate Biz Card

-Card Size: Standard
-Background: Dark grey or black. I am open to gradient or a textured background.
-Other Colors: I dont mind pops of color. Contrasty blue, lime green, red Etc. Feel free to get creative.
-Text color: be creative
-Font: I like modern styles. Something that works well with my KV718 logo. See attached
-I would like my logo (KV718) watermarked on the card. Either on one side or both.
-Front of Card: keep it simple. Head shot, name, Logo, Phone #
-Back: add the rest of the details. See list below.
-brokerages logo as well as the Domivest and Equal Housing Opportunity logos on the card
-Name: Tod Marwick
-Residential Real Estate
-Cell:
-Email:
-Site:
-Office Address:
-very small/fine print "Each office independently owned & operated

```html
<!DOCTYPE html>
<html lang="en">
<head>
<meta charset="utf-8">
<title>KV718 Business Card</title>
<link href="https://fonts.googleapis.com/css2?family=Mulish:wght@400;700&family=Josefin+Sans:wght@600&display=swap" rel="stylesheet">
<style>
  :root {
    --page: #ffffff;
    --card-dark: #0c0c0c;
    --card-mid: #262626;
    --accent: #ff0a0a;
    --ink: #ffffff;
    --photo-top: #2b2d33;
    --photo-mid: #8f7663;
    --photo-low: #4f6aa6;
  }
  html, body {
    margin: 0;
    width: 1200px;
    height: 1200px;
    overflow: hidden;
    background: var(--page);
  }
  .canvas { position: relative; width: 1200px; height: 1200px; }
  .card {
    position: absolute;
    left: 198px;
    width: 804px;
    height: 510px;
    overflow: hidden;
    background: radial-gradient(ellipse at 75% 20%, var(--card-mid) 0%, #161616 45%, var(--card-dark) 100%);
    font-family: "Mulish", sans-serif;
    color: var(--ink);
  }
  .card--contact { top: 72px; }
  .card--portrait { top: 618px; }

  .holder-name {
    position: absolute;
    left: 80px;
    top: 66px;
    margin: 0;
    font-family: "Josefin Sans", sans-serif;
    font-weight: 600;
    font-size: 40px;
    letter-spacing: 3px;
  }
  .contact-list { list-style: none; margin: 0; padding: 0; }
  .contact-item {
    position: absolute;
    left: 0;
    height: 48px;
    display: flex;
    align-items: center;
    font-size: 26px;
  }
  .contact-badge {
    width: 64px;
    height: 48px;
    margin-right: 16px;
    background: var(--accent);
    border-radius: 0 24px 24px 0;
    display: flex;
    align-items: center;
    justify-content: center;
  }
  .contact-badge svg { width: 26px; height: 26px; }

  .brand-name {
    position: absolute;
    margin: 0;
    font-family: "Josefin Sans", sans-serif;
    font-weight: 600;
    color: var(--accent);
    line-height: 1;
    letter-spacing: 2px;
  }
  .card--contact .brand-name { right: 50px; top: 470px; font-size: 86px; transform: translateY(-100%); }
  .card--portrait .brand-name { left: 86px; top: 212px; font-size: 86px; }

  .accent-band {
    position: absolute;
    left: 0;
    height: 16px;
    background: var(--accent);
  }
  .card--contact .accent-band { top: 486px; width: 100%; }
  .card--portrait .accent-band { top: 486px; width: 426px; }

  .portrait-photo {
    position: absolute;
    right: 0;
    top: 30px;
    width: 384px;
    height: 480px;
    background:
      radial-gradient(ellipse 30% 36% at 55% 32%, var(--photo-mid) 0%, rgba(143,118,99,0) 100%),
      linear-gradient(180deg, var(--photo-top) 0%, var(--photo-top) 55%, var(--photo-low) 75%, var(--photo-low) 100%);
  }
</style>
</head>
<body>
<main class="canvas">
  <section class="card card--contact">
    <h1 class="holder-name">TOD MARWICK</h1>
    <ul class="contact-list">
      <li class="contact-item" style="top:141px">
        <span class="contact-badge">
          <svg viewBox="0 0 24 24" fill="none" stroke="#fff" stroke-width="2"><rect x="7" y="2" width="10" height="20" rx="2"/><circle cx="12" cy="18" r="0.8" fill="#fff"/></svg>
        </span>012 345 6789
      </li>
      <li class="contact-item" style="top:205px">
        <span class="contact-badge">
          <svg viewBox="0 0 24 24"><path d="M12 2a8 8 0 0 0-8 8c0 6 8 12 8 12s8-6 8-12a8 8 0 0 0-8-8z" fill="#fff"/><circle cx="12" cy="10" r="4" fill="#ff0a0a"/></svg>
        </span>Somewhere Street 12, City, Country
      </li>
      <li class="contact-item" style="top:269px">
        <span class="contact-badge">
          <svg viewBox="0 0 24 24" fill="none" stroke="#fff" stroke-width="2.4"><circle cx="12" cy="12" r="4"/><path d="M16 8v5a2.5 2.5 0 0 0 5 0v-1a9 9 0 1 0-3.5 7.1"/></svg>
        </span>info@kv718.com
      </li>
      <li class="contact-item" style="top:333px">
        <span class="contact-badge">
          <svg viewBox="0 0 24 24" fill="none" stroke="#fff" stroke-width="2.2" stroke-linecap="round"><path d="M10 14a4 4 0 0 0 5.7 0l3-3a4 4 0 0 0-5.7-5.7l-1 1"/><path d="M14 10a4 4 0 0 0-5.7 0l-3 3a4 4 0 0 0 5.7 5.7l1-1"/></svg>
        </span>www.kv718.com
      </li>
    </ul>
    <p class="brand-name">KV718</p>
    <div class="accent-band"></div>
  </section>

  <section class="card card--portrait">
    <p class="brand-name">KV718</p>
    <div class="accent-band"></div>
    <div class="portrait-photo" role="img" aria-label="Head-and-shoulders portrait of the agent smiling, wearing a blue checked shirt"></div>
  </section>
</main>
</body>
</html>
```